New Business Cards for Velmora

About Velmora:
At Velmora, we're more than just a company—we're a force for positive change in the staffing industry. Our brand is our heartbeat, and we need a designer who can translate that into every design element.

The Project:
We're revamping our business cards and need your artistic flair to make them stand out. Here's what we're looking for:

- Incorporate our existing brand elements (logo, colours, fonts) into the design.
- Craft a design that's sleek, professional, and memorable.
- Provide options for different layouts and finishes.
- Collaborate closely with our team to ensure the final product exceeds expectations.

Please note: For general text, we use Avenir. The brand guidelines are slightly out of date and don't have correct imaging. Colours are correct though.

```html
<!DOCTYPE html>
<html lang="en">
<head>
<meta charset="utf-8">
<title>Velmora Business Cards</title>
<link rel="stylesheet" href="https://fonts.googleapis.com/css2?family=Nunito+Sans:wght@400;700;800&display=swap">
<style>
  :root {
    --page-bg: #f1f1f2;
    --card-bg: #ffffff;
    --brand-purple: #5f2b73;
    --brand-plum: #6a2c78;
    --brand-magenta: #c2387a;
    --ink-light: #ffffff;
  }
  * { margin: 0; padding: 0; box-sizing: border-box; }
  html, body {
    width: 1200px; height: 1200px; overflow: hidden;
    background: var(--page-bg);
    font-family: "Nunito Sans", "Avenir", sans-serif;
  }
  .canvas { position: relative; width: 1200px; height: 1200px; }
  .card {
    position: absolute; left: 154px; width: 894px; height: 535px;
    background: var(--card-bg);
    box-shadow: 0 4px 14px rgba(0,0,0,0.18);
    overflow: hidden;
  }
  .card--front { top: 44px; }
  .card--back { top: 612px; }
  .card-shapes { position: absolute; inset: 0; width: 894px; height: 535px; }

  .wordmark {
    position: absolute;
    color: var(--brand-purple); font-weight: 700; letter-spacing: -1px; line-height: 1;
  }
  .card--front .wordmark { left: 56px; top: 96px; font-size: 66px; }
  .card--back .wordmark { left: 96px; top: 222px; font-size: 80px; }

  .contact { position: absolute; right: 64px; text-align: right; color: var(--ink-light); }
  .contact__name { top: 127px; font-size: 35px; font-weight: 800; line-height: 47px; }
  .contact__role { top: 218px; font-size: 21px; font-weight: 400; line-height: 28px; }
  .contact__list { list-style: none; top: 298px; font-size: 21px; right: 62px; }
  .contact__list li { display: flex; justify-content: flex-end; align-items: center; gap: 14px; height: 28px; }
  .contact__list li.gap { margin-top: 38px; }
  .contact__list li.nudge { margin-right: 28px; }
  .icon { width: 14px; height: 14px; fill: var(--ink-light); flex: none; }
</style>
</head>
<body>
<main class="canvas">

  <section class="card card--front">
    <svg class="card-shapes" viewBox="0 0 894 535" aria-hidden="true">
      <defs>
        <linearGradient id="panelFront" x1="0" y1="0" x2="0" y2="1">
          <stop offset="0" stop-color="#6a2c78"/>
          <stop offset="1" stop-color="#c2387a"/>
        </linearGradient>
      </defs>
      <path d="M700 234 H388 Q364 234 353 256 L218 500 Q204 533 244 533 H520" fill="none" stroke="url(#panelFront)" stroke-width="2.5"/>
      <path d="M590 0 H894 V535 H372 Q315 535 333 493 L530 40 Q547 0 590 0 Z" fill="url(#panelFront)"/>
    </svg>

    <div class="wordmark">Velmora</div>

    <h1 class="contact contact__name">Dorian<br>Fellowes</h1>
    <p class="contact contact__role">Founder &amp; Director</p>
    <ul class="contact contact__list">
      <li>3/C, Address, Street
        <svg class="icon" viewBox="0 0 14 14"><path d="M7 0C4.2 0 2.2 2 2.2 4.7 2.2 8.2 7 14 7 14s4.8-5.8 4.8-9.3C11.8 2 9.8 0 7 0zm0 6.6A1.9 1.9 0 1 1 7 2.8a1.9 1.9 0 0 1 0 3.8z"/></svg>
      </li>
      <li class="nudge">Pin - 123456</li>
      <li class="gap">1234-567-890
        <svg class="icon" viewBox="0 0 14 14"><path d="M3 0.5l2.2 2.8-1.3 1.7c.8 1.8 2.3 3.3 4.1 4.1l1.7-1.3 2.8 2.2-1.3 2.5C6 12 2 8 1.5 1.8z"/></svg>
      </li>
      <li>info@velmoragroup.com
        <svg class="icon" viewBox="0 0 14 14"><path d="M1 2.5h12v9H1z M1.5 3l5.5 4.2L12.5 3"/></svg>
      </li>
      <li>www.velmoragroup.com
        <svg class="icon" viewBox="0 0 14 14"><circle cx="7" cy="7" r="6.2"/><path d="M1 7h12M7 1c-2.4 2.8-2.4 9.2 0 12M7 1c2.4 2.8 2.4 9.2 0 12" fill="none" stroke="#a63479" stroke-width="1"/></svg>
      </li>
    </ul>
  </section>

  <section class="card card--back">
    <svg class="card-shapes" viewBox="0 0 894 535" aria-hidden="true">
      <defs>
        <linearGradient id="panelBack" x1="0" y1="0" x2="0" y2="1">
          <stop offset="0" stop-color="#6a2c78"/>
          <stop offset="1" stop-color="#c2387a"/>
        </linearGradient>
      </defs>
      <path d="M696 0 L537 345 Q518 415 592 415 H860" fill="none" stroke="url(#panelBack)" stroke-width="2.5"/>
      <path d="M862 120 H894 V535 H640 L815 152 Q830 120 862 120 Z" fill="url(#panelBack)"/>
    </svg>

    <div class="wordmark">Velmora</div>
  </section>

</main>
</body>
</html>
```